Global Marketing company needs a new look!

Please see attached brief for a new design of our website and other materials. This will include icons, appearance, structure etc. We are a global, leading marketing agency with a passion for innovation and giving our clients the best ROI possible. Please make it elegant as we want to attract high end customers- some of our clients include Vorlumo, KT cars and Bellamundo so these are the preminum clients we are aiming for and so we don't want it to look cheap or tacky.

Industry/Entity Type

It Company

Number of Pages Required

1 page

Colors
ffc214
ffffff
474747

Requirements
Nice to have
• Icons to represent sales, increases etc

```html
<!DOCTYPE html>
<html lang="en">
<head>
<meta charset="utf-8">
<title>Strevo – Digital Performance Re-invented</title>
<link rel="stylesheet" href="https://fonts.googleapis.com/css2?family=Open+Sans:wght@400;600;700&family=Roboto:wght@300;400;500;700&display=swap">
<style>
:root{
  --yellow:#ffc214;
  --orange:#f6b12b;
  --white:#ffffff;
  --charcoal:#474747;
  --nav:#3d3d3d;
  --ink:#1f1f1f;
  --blue:#1da1dc;
  --line:#d9d9d9;
  --teal:#9fcfcc;
  --black:#050505;
}
*{margin:0;padding:0;box-sizing:border-box}
html,body{width:1200px;height:2632px;overflow:hidden;background:var(--white)}
body{position:relative;font-family:"Open Sans",Arial,sans-serif;color:var(--ink)}
.abs{position:absolute}

/* header */
.brand-tab{left:0;top:0;width:415px;height:77px}
.brand-name{left:205px;top:14px;font:700 34px/1 "Open Sans",Arial,sans-serif;color:var(--white)}
.contact-row{top:18px;font:400 13px/1 "Open Sans",Arial,sans-serif;color:var(--blue);display:flex;align-items:center;gap:10px}
.search{left:954px;top:12px;width:176px;height:32px;display:flex;align-items:center;justify-content:space-between;font:400 13px/1 "Open Sans",sans-serif;color:var(--blue)}
.main-nav{left:0;top:58px;width:1200px;height:49px}
.nav-links{left:410px;top:58px;height:49px;display:flex;align-items:center;gap:0;font:500 15px/1 "Roboto",Arial,sans-serif;color:var(--white)}
.nav-links span{display:flex;align-items:center;gap:4px;margin-right:30px}
.nav-phone{left:968px;top:75px;font:700 15px/1 "Roboto",sans-serif;color:var(--white)}

/* hero */
.hero-bg{left:0;top:107px;width:1200px;height:708px}
.join-panel{left:72px;top:149px;width:368px;height:426px;background:rgba(70,70,70,.88);padding:36px 36px}
.join-panel h2{font:700 21px/1 "Open Sans",sans-serif;color:var(--white);margin-bottom:18px}
.join-panel p{font:400 13px/22px "Open Sans",sans-serif;color:#e5e5e5;margin-bottom:26px}
.field{height:48px;background:var(--white);margin-bottom:11px;font:400 15px/48px "Open Sans",sans-serif;color:#222;padding-left:14px}
.join-btn{margin-top:18px;width:180px;height:52px;background:var(--blue);color:var(--white);font:400 22px/52px "Roboto",sans-serif;display:flex;align-items:center;justify-content:center;gap:12px}
.video-thumb{left:72px;top:596px;width:368px;height:172px;background:linear-gradient(90deg,#4a5560 0%,#1f4e7a 45%,#1a6fb1 100%)}
.video-bar{left:72px;top:752px;width:368px;height:16px;background:var(--white)}
.dots{left:74px;top:779px;display:flex;gap:12px}
.dots i{width:13px;height:13px;border-radius:50%;background:var(--white);display:block}
.dots i.on{background:var(--blue)}
.hero-copy{left:595px;top:180px;width:530px;text-align:center;color:var(--white)}
.hero-logo{display:flex;align-items:center;justify-content:center;gap:18px;height:90px}
.hero-logo hr{flex:1;border:0;border-top:2px solid rgba(255,255,255,.85)}
.hero-logo b{font:700 46px/1 "Open Sans",sans-serif}
.hero-title{margin-top:48px;font:400 70px/76px "Roboto",sans-serif;letter-spacing:1px}
.hero-rule{margin:44px auto 0;border:0;border-top:2px solid rgba(255,255,255,.85);width:530px}
.hero-tags{margin-top:24px;font:400 26px/41px "Roboto",sans-serif;color:var(--orange);letter-spacing:1px}

/* buttons */
.btn{background:var(--blue);color:var(--white);font:600 13px/1 "Open Sans",sans-serif;display:flex;align-items:center;justify-content:center;gap:42px}

/* network section */
.devices{left:74px;top:965px;width:601px;height:307px}
.network-copy{left:702px;top:975px;width:440px}
.network-copy h3{font:700 22px/34px "Open Sans",sans-serif;color:var(--orange)}
.network-copy p{margin-top:26px;font:400 14px/19px "Open Sans",sans-serif;color:#222}
.network-copy .btn{margin-top:32px;width:181px;height:32px}

/* talent band */
.talent-band{left:0;top:1368px;width:1200px;height:311px}
.talent-copy{left:0;top:1468px;width:1200px;text-align:center;color:var(--white)}
.talent-copy h3{font:700 22px/1 "Open Sans",sans-serif;letter-spacing:.3px}
.talent-copy p{margin-top:18px;font:400 15px/1 "Open Sans",sans-serif}
.talent-copy .btn{margin:44px auto 0;width:179px;height:28px}

/* results */
.results-title{left:0;top:1810px;width:1200px;text-align:center;font:700 33px/1 "Open Sans",sans-serif;color:var(--orange);letter-spacing:1px}
.result-card{top:1919px;width:249px;height:270px;border:2px solid var(--line);text-align:center}
.result-card .icon{position:absolute;left:64px;top:22px;width:120px;height:92px;background:linear-gradient(180deg,#9fcfcc,#6fa9a6);border-radius:6px}
.result-card p{position:absolute;left:10px;top:150px;width:225px;font:600 13px/21px "Open Sans",sans-serif;color:#111}
.result-card .btn{position:absolute;left:44px;top:217px;width:181px;height:28px;gap:52px}

/* footer */
.to-top{left:1083px;top:2257px;width:40px;height:40px}
.footer-bg{left:0;top:2281px;width:1200px;height:351px}
.footer-brand{left:74px;top:2375px;font:700 96px/1 "Open Sans",sans-serif;color:var(--white);letter-spacing:-1px}
.newsletter{left:609px;top:2316px;width:520px;color:var(--white)}
.newsletter h4{font:600 22px/1 "Open Sans",sans-serif}
.newsletter p{margin-top:29px;font:400 13px/22px "Open Sans",sans-serif}
.subscribe{display:flex;gap:9px;margin-top:17px}
.subscribe .email{width:326px;height:37px;background:var(--white);font:400 13px/37px "Open Sans",sans-serif;color:#999;padding-left:14px}
.subscribe .go{width:180px;height:37px;background:var(--orange);font:700 16px/37px "Roboto",sans-serif;text-align:center;color:var(--white)}
.social{display:flex;gap:23px;margin-top:40px;margin-left:0}
.social i{display:block;width:47px;height:47px;border-radius:50%;background:#e4e4e4;border:3px solid #bdbdbd}
.legal{left:609px;top:2593px;font:400 13px/1 "Open Sans",sans-serif;color:var(--white)}
.legal b{font-weight:600}
</style>
</head>
<body>

<!-- header -->
<svg class="abs brand-tab" viewBox="0 0 415 77" aria-hidden="true"><polygon points="0,0 415,0 360,77 0,77" fill="var(--yellow)"/></svg>
<div class="abs brand-name">strevo</div>

<div class="abs contact-row" style="left:520px">
  <svg width="22" height="16" viewBox="0 0 22 16"><rect x="1" y="1" width="20" height="14" fill="none" stroke="var(--blue)" stroke-width="2"/><polyline points="1,1 11,9 21,1" fill="none" stroke="var(--blue)" stroke-width="2"/></svg>
  <span>hello@strevo.org</span>
</div>
<div class="abs contact-row" style="left:760px">
  <svg width="16" height="16" viewBox="0 0 24 24"><path d="M6.6 10.8a15 15 0 0 0 6.6 6.6l2.2-2.2c.3-.3.7-.4 1-.2 1.1.4 2.3.6 3.6.6.6 0 1 .4 1 1V20c0 .6-.4 1-1 1A17 17 0 0 1 3 4c0-.6.4-1 1-1h3.5c.6 0 1 .4 1 1 0 1.3.2 2.5.6 3.6.1.3 0 .7-.2 1z" fill="var(--blue)"/></svg>
  <span>1-888-5550-142</span>
</div>
<div class="abs search"><span>Search ...</span>
  <svg width="18" height="18" viewBox="0 0 18 18"><circle cx="7" cy="7" r="5.5" fill="none" stroke="var(--blue)" stroke-width="2"/><line x1="11" y1="11" x2="17" y2="17" stroke="var(--blue)" stroke-width="2.4"/></svg>
</div>

<svg class="abs main-nav" viewBox="0 0 1200 49" aria-hidden="true"><polygon points="396,0 1200,0 1200,49 360,49" fill="var(--nav)"/></svg>
<nav class="abs nav-links">
  <span>SERVICES <svg width="9" height="6" viewBox="0 0 9 6"><polyline points="1,1 4.5,4.5 8,1" fill="none" stroke="#fff" stroke-width="1.8"/></svg></span>
  <span>TEAM <svg width="9" height="6" viewBox="0 0 9 6"><polyline points="1,1 4.5,4.5 8,1" fill="none" stroke="#fff" stroke-width="1.8"/></svg></span>
  <span>TECH <svg width="9" height="6" viewBox="0 0 9 6"><polyline points="1,1 4.5,4.5 8,1" fill="none" stroke="#fff" stroke-width="1.8"/></svg></span>
  <span style="margin-right:12px">BLOG <svg width="9" height="6" viewBox="0 0 9 6"><polyline points="1,1 4.5,4.5 8,1" fill="none" stroke="#fff" stroke-width="1.8"/></svg></span>
  <span>JOIN US <svg width="9" height="6" viewBox="0 0 9 6"><polyline points="1,1 4.5,4.5 8,1" fill="none" stroke="#fff" stroke-width="1.8"/></svg></span>
  <span>CONTACT <svg width="9" height="6" viewBox="0 0 9 6"><polyline points="1,1 4.5,4.5 8,1" fill="none" stroke="#fff" stroke-width="1.8"/></svg></span>
</nav>
<div class="abs nav-phone">UK: +44 20 5550 1234</div>

<!-- hero -->
<svg class="abs hero-bg" viewBox="0 0 1200 708" role="img" aria-label="Photo of a businessman in a suit holding a glowing globe network">
  <defs>
    <linearGradient id="heroTone" x1="0" y1="0" x2="1" y2="1">
      <stop offset="0" stop-color="#7f95a6"/>
      <stop offset=".5" stop-color="#4c6678"/>
      <stop offset="1" stop-color="#2b3f50"/>
    </linearGradient>
  </defs>
  <polygon points="0,0 1200,0 1200,686 396,686 360,708 0,708" fill="url(#heroTone)"/>
</svg>

<form class="abs join-panel">
  <h2>Request a Join</h2>
  <p>Get in touch with us if you have any queries and<br>we will get back to you as soon as possible.</p>
  <div class="field">Full Name</div>
  <div class="field">E-mail</div>
  <div class="field">Phone</div>
  <div class="join-btn">JOIN NOW
    <svg width="24" height="20" viewBox="0 0 24 20"><path d="M6 15H5a4 4 0 0 1 0-8 6 6 0 0 1 11.5-1.5A4.5 4.5 0 0 1 19 15h-1" fill="none" stroke="#fff" stroke-width="1.8"/><polyline points="9,13 12,16 15,13" fill="none" stroke="#fff" stroke-width="1.8"/><line x1="12" y1="9" x2="12" y2="16" stroke="#fff" stroke-width="1.8"/></svg>
  </div>
</form>

<div class="abs video-thumb" role="img" aria-label="Video still of a support agent with headset beside a world network graphic"></div>
<div class="abs video-bar"></div>
<div class="abs dots"><i class="on"></i><i></i><i></i><i></i></div>

<div class="abs hero-copy">
  <div class="hero-logo"><hr><b>strevo</b><hr></div>
  <h1 class="hero-title">DIGITAL<br>PERFORMANCE<br>RE-INVENTED</h1>
  <hr class="hero-rule">
  <div class="hero-tags">PPC &nbsp;.&nbsp;&nbsp; DISPLAY . &nbsp;PAID SOCIAL<br>SEO &nbsp;.&nbsp;&nbsp; CONTENT &nbsp;.&nbsp;&nbsp; ANALYTICS</div>
</div>

<!-- network -->
<div class="abs devices" role="img" aria-label="Illustration of a tablet, laptop and phone showing a world map with location markers" style="background:linear-gradient(180deg,#9fcfcc 0%,#8dc2bf 100%);border:14px solid #1d1d1d;border-radius:14px"></div>
<div class="abs network-copy">
  <h3>FIRST – WE HAVE THE ONLY WORLDWIDE<br>NETWORK OF DIGITAL SPECIALISTS</h3>
  <p>With over 600 specialists in 75 countries speaking 80 languages – we deliver global and local cross-channel campaigns. Because there is never a substitute for truly local expertise</p>
  <div class="btn">READ MORE
    <svg width="22" height="18" viewBox="0 0 24 20"><path d="M6 15H5a4 4 0 0 1 0-8 6 6 0 0 1 11.5-1.5A4.5 4.5 0 0 1 19 15h-1" fill="none" stroke="#fff" stroke-width="1.8"/><polyline points="9,13 12,16 15,13" fill="none" stroke="#fff" stroke-width="1.8"/><line x1="12" y1="9" x2="12" y2="16" stroke="#fff" stroke-width="1.8"/></svg>
  </div>
</div>

<!-- talent -->
<svg class="abs talent-band" viewBox="0 0 1200 311" role="img" aria-label="Dark photo of a city skyline with business people silhouettes">
  <defs>
    <linearGradient id="bandTone" x1="0" y1="0" x2="1" y2="0">
      <stop offset="0" stop-color="#2a2a2a"/>
      <stop offset=".5" stop-color="#3a3a3a"/>
      <stop offset="1" stop-color="#252525"/>
    </linearGradient>
  </defs>
  <polygon points="0,18 448,18 480,0 1200,0 1200,290 720,290 690,311 0,311" fill="url(#bandTone)"/>
</svg>
<div class="abs talent-copy">
  <h3>SECOND – WE RECRUIT AND RETAIN THE FINEST IN-HOUSE TALENT</h3>
  <p>Everyone in the team is a shareholder – so when you win we win – giving us a staff retention of 96% and unrivalled account management continuity</p>
  <div class="btn">READ MORE
    <svg width="22" height="18" viewBox="0 0 24 20"><path d="M6 15H5a4 4 0 0 1 0-8 6 6 0 0 1 11.5-1.5A4.5 4.5 0 0 1 19 15h-1" fill="none" stroke="#fff" stroke-width="1.8"/><polyline points="9,13 12,16 15,13" fill="none" stroke="#fff" stroke-width="1.8"/><line x1="12" y1="9" x2="12" y2="16" stroke="#fff" stroke-width="1.8"/></svg>
  </div>
</div>

<!-- results -->
<h2 class="abs results-title">THE RESULT 5 YEARS LATER?</h2>

<div class="abs result-card" style="left:72px">
  <div class="icon" role="img" aria-label="Illustration of a presentation easel"></div>
  <p>Norvexa's Fastest Growing Agency</p>
  <div class="btn">READ MORE<svg width="22" height="18" viewBox="0 0 24 20"><path d="M6 15H5a4 4 0 0 1 0-8 6 6 0 0 1 11.5-1.5A4.5 4.5 0 0 1 19 15h-1" fill="none" stroke="#fff" stroke-width="1.8"/><polyline points="9,13 12,16 15,13" fill="none" stroke="#fff" stroke-width="1.8"/><line x1="12" y1="9" x2="12" y2="16" stroke="#fff" stroke-width="1.8"/></svg></div>
</div>
<div class="abs result-card" style="left:340px">
  <div class="icon" role="img" aria-label="Illustration of a world map with location pins"></div>
  <p>Hubs in London, New York,<br>Sydney and Singapore</p>
  <div class="btn">READ MORE<svg width="22" height="18" viewBox="0 0 24 20"><path d="M6 15H5a4 4 0 0 1 0-8 6 6 0 0 1 11.5-1.5A4.5 4.5 0 0 1 19 15h-1" fill="none" stroke="#fff" stroke-width="1.8"/><polyline points="9,13 12,16 15,13" fill="none" stroke="#fff" stroke-width="1.8"/><line x1="12" y1="9" x2="12" y2="16" stroke="#fff" stroke-width="1.8"/></svg></div>
</div>
<div class="abs result-card" style="left:609px">
  <div class="icon" role="img" aria-label="Illustration of a laptop surrounded by expert markers"></div>
  <p>Over 600 experts in every<br>digital discipline</p>
  <div class="btn">READ MORE<svg width="22" height="18" viewBox="0 0 24 20"><path d="M6 15H5a4 4 0 0 1 0-8 6 6 0 0 1 11.5-1.5A4.5 4.5 0 0 1 19 15h-1" fill="none" stroke="#fff" stroke-width="1.8"/><polyline points="9,13 12,16 15,13" fill="none" stroke="#fff" stroke-width="1.8"/><line x1="12" y1="9" x2="12" y2="16" stroke="#fff" stroke-width="1.8"/></svg></div>
</div>
<div class="abs result-card" style="left:877px">
  <div class="icon" role="img" aria-label="Illustration of a chart screen and calculator"></div>
  <p>Reputation for treating clients'<br>money like it's our own!</p>
  <div class="btn">READ MORE<svg width="22" height="18" viewBox="0 0 24 20"><path d="M6 15H5a4 4 0 0 1 0-8 6 6 0 0 1 11.5-1.5A4.5 4.5 0 0 1 19 15h-1" fill="none" stroke="#fff" stroke-width="1.8"/><polyline points="9,13 12,16 15,13" fill="none" stroke="#fff" stroke-width="1.8"/><line x1="12" y1="9" x2="12" y2="16" stroke="#fff" stroke-width="1.8"/></svg></div>
</div>

<!-- footer -->
<svg class="abs footer-bg" viewBox="0 0 1200 351" aria-hidden="true"><polygon points="0,22 812,22 848,0 1200,0 1200,351 0,351" fill="var(--black)"/></svg>
<svg class="abs to-top" viewBox="0 0 40 40" aria-label="Back to top"><circle cx="20" cy="20" r="20" fill="var(--orange)"/><polyline points="12,24 20,16 28,24" fill="none" stroke="#111" stroke-width="3.5"/></svg>

<div class="abs footer-brand">strevo</div>

<section class="abs newsletter">
  <h4>Newsletter</h4>
  <p>Keep up on our always evolving product features and technology.<br>Enter your e-mail and subscribe to our newsletter.</p>
  <div class="subscribe"><div class="email">Email Address</div><div class="go">SUBSCRIBE</div></div>
  <div class="social"><i></i><i></i><i></i><i></i><i></i></div>
</section>
<div class="abs legal">Copyright © Strevo Inc Ltd 2016. All Rights Reserved / <b>LOGIN</b> &nbsp;&nbsp;&nbsp;&nbsp; | &nbsp;&nbsp;&nbsp; <b>PRIVACY POLICY</b></div>

</body>
</html>
```